Needing a business Card for new fire company.

Dalvo, sales fire equipment and parts. We also do tree clearing for the forest service. My logo will be attached to this. I am also looking for a design that when people see the card it stick with them and they will remember my sales team giving it to them.

```html
<!DOCTYPE html>
<html lang="en">
<head>
<meta charset="utf-8">
<title>Dalvo Business Card</title>
<link href="https://fonts.googleapis.com/css2?family=Montserrat:wght@800&family=Arimo:wght@400;700&display=swap" rel="stylesheet">
<style>
  :root {
    --stage: #c4c4c4;
    --paper: #ffffff;
    --ink: #1b1b1b;
    --fire-red: #c8202a;
    --edge-red: #e0242c;
    --charcoal: #2b2b2b;
    --charcoal-deep: #232323;
  }
  * { margin: 0; padding: 0; box-sizing: border-box; }
  html, body {
    width: 1200px; height: 800px; overflow: hidden;
    background: var(--stage);
  }
  .canvas {
    position: relative; width: 1200px; height: 800px;
    display: flex; align-items: center; justify-content: center; gap: 50px;
  }
  .card {
    position: relative; width: 525px; height: 300px;
    border-bottom: 3px solid var(--edge-red);
    border-left: 3px solid var(--edge-red);
    box-shadow: 0 10px 24px rgba(0,0,0,0.25);
    overflow: hidden;
  }
  .card-front { background: var(--paper); color: var(--ink); font-family: "Arimo", Arial, sans-serif; }
  .card-back { background: var(--charcoal); }

  .brand {
    position: absolute; top: 38px; right: 42px;
    display: flex; flex-direction: column; align-items: stretch;
  }
  .brand-rule { height: 2px; background: var(--fire-red); }
  .brand-name {
    font-family: "Montserrat", Arial, sans-serif; font-weight: 800;
    font-size: 58px; letter-spacing: 3px; line-height: 1;
    color: var(--ink); padding: 8px 6px 6px;
  }
  .divider {
    position: absolute; left: 28px; right: 0; top: 178px;
    height: 1.5px; background: var(--fire-red);
  }
  .person { position: absolute; left: 36px; top: 120px; }
  .person-name {
    font-family: "Montserrat", Arial, sans-serif; font-weight: 800;
    font-size: 22px; color: var(--fire-red); letter-spacing: 0.5px;
  }
  .person-title { font-size: 15px; margin-top: 2px; }
  .contacts { position: absolute; left: 36px; top: 194px; list-style: none; }
  .contacts li { display: flex; align-items: center; gap: 8px; font-size: 15px; line-height: 24px; }
  .contacts svg { width: 15px; height: 15px; fill: var(--fire-red); flex: none; }
  .accent { color: var(--fire-red); }
  .address { position: absolute; right: 30px; top: 196px; font-size: 14px; line-height: 20px; }
  .address span { display: block; }
  .address span + span { padding-left: 40px; }

  .pattern-field {
    position: absolute; inset: 0;
    background: linear-gradient(135deg, var(--charcoal) 0%, var(--charcoal-deep) 100%);
  }
  .back-brand {
    position: absolute; left: 50%; top: 50%; transform: translate(-50%, -50%);
    display: flex; flex-direction: column; align-items: stretch;
  }
  .back-brand .brand-name { color: #ffffff; font-size: 36px; padding: 5px 4px 4px; }
</style>
</head>
<body>
<main class="canvas">
  <section class="card card-front" aria-label="Card front">
    <div class="brand">
      <div class="brand-rule"></div>
      <div class="brand-name">DALVO</div>
      <div class="brand-rule"></div>
    </div>

    <div class="person">
      <div class="person-name">MARCUS HALE</div>
      <div class="person-title">Managing Director</div>
    </div>

    <div class="divider"></div>

    <ul class="contacts">
      <li>
        <svg viewBox="0 0 24 24" aria-hidden="true"><path d="M6.6 10.8a15.1 15.1 0 0 0 6.6 6.6l2.2-2.2a1 1 0 0 1 1-.25 11.4 11.4 0 0 0 3.6.57 1 1 0 0 1 1 1V20a1 1 0 0 1-1 1A17 17 0 0 1 3 4a1 1 0 0 1 1-1h3.5a1 1 0 0 1 1 1c0 1.25.2 2.45.57 3.57a1 1 0 0 1-.25 1z"/></svg>
        044-987 654 321
      </li>
      <li>
        <svg viewBox="0 0 24 24" aria-hidden="true"><path d="M2 5h20v14H2zM4 7v.5l8 5 8-5V7z"/></svg>
        info@dalvofire.com
      </li>
      <li>
        <svg viewBox="0 0 24 24" aria-hidden="true"><path d="M12 2a10 10 0 1 0 0 20 10 10 0 0 0 0-20zm6.9 6h-2.9a15.7 15.7 0 0 0-1.4-3.6A8 8 0 0 1 18.9 8zM12 4c.8 1.2 1.5 2.5 1.9 4h-3.8c.4-1.5 1.1-2.8 1.9-4zM4.3 14a8 8 0 0 1 0-4h3.4a16 16 0 0 0 0 4zm.8 2h2.9c.3 1.3.8 2.5 1.4 3.6A8 8 0 0 1 5.1 16zM8 8H5.1a8 8 0 0 1 4.3-3.6C8.8 5.5 8.3 6.7 8 8zm4 12c-.8-1.2-1.5-2.5-1.9-4h3.8c-.4 1.5-1.1 2.8-1.9 4zm2.3-6H9.7a14 14 0 0 1 0-4h4.6a14 14 0 0 1 0 4zm.3 5.6c.6-1.1 1.1-2.3 1.4-3.6h2.9a8 8 0 0 1-4.3 3.6zm1.7-5.6a16 16 0 0 0 0-4h3.4a8 8 0 0 1 0 4z"/></svg>
        <span>www.<span class="accent">dalvofire</span>.com</span>
      </li>
    </ul>

    <div class="address">
      <span>218, Cedar Ridge Road</span>
      <span>60814, Pinewood Valley</span>
    </div>
  </section>

  <section class="card card-back" aria-label="Card back">
    <div class="pattern-field" role="img" aria-label="Embossed repeating brand pattern in dark charcoal tones"></div>
    <div class="back-brand">
      <div class="brand-rule"></div>
      <div class="brand-name">DALVO</div>
      <div class="brand-rule"></div>
    </div>
  </section>
</main>
</body>
</html>
```